依頼詳細
RPE歯科クリニック~行きます訪問歯科・送迎歯科~
のパンフレットを作成依頼致します。

1.パンフレットに使用したいデータ等がございません。以前使用していたパンフレットをPDFで添付いたしますのでご確認ください。添付エクセルデータがございます。こちらを参考にA4両面に収めてレイアウトしてください。

2. パンフレットは以前のパンフレットの(ピンク×水色、ピンク、水色)を希望しております。

3.1枚目の車のロゴはないので、作成いただいてもフリー素材でも結構ですのでお願い致します。

4.MAPは、添付フィル≪MAP_image≫をご確認ください。

5.仕上がりはA4両面イラストレーターデザインを希望いたします。フルカラーでお願いします。
サイズ
A4
ページ数
4ページ
希望イメージ
シンプル 複雑
単色 カラフル
暗い 明るい
日常 高級
遊び心 厳粛
未来的 伝統的
女性的 男性的
希望する色
赤系、水色系
納品ファイル
• イラストレーター形式 (.ai)
補足説明
修正致します

1.添付エクセルデータがございます。→PDFデータの為、文字おこしお願い致します。
医院名
RPE歯科クリニック
~行きます訪問歯科・送迎歯科~
パンフレットのカテゴリになっておりますが、
A4サイズ両面のチラシ作成依頼になります。

よろしくお願いいたします。
コンペ当選者を確約に変更いたしましたのでよろしくお願いいたします。

色使いや、歯を使ったイラストの可愛さと、全体的に見やすくバランスが良かったです。

たくさんのご提案ありがとうございました。 慣れない依頼にご提案くださり感謝しています。 また、機会がありましたら是非ご協力ください。 ありがとうございました。

```html
<!DOCTYPE html>
<html lang="ja">
<head>
<meta charset="UTF-8">
<title>RPE歯科医院 訪問・送迎歯科クリニック</title>
<link href="https://fonts.googleapis.com/css2?family=M+PLUS+Rounded+1c:wght@400;500;700&display=swap" rel="stylesheet">
<style>
  :root {
    --pink: #ee8fa6;
    --pink-deep: #e77894;
    --pink-soft: #f8d3dc;
    --pink-wash: #fbe6ec;
    --pink-line: #f3bfcc;
    --ink: #4a4a4a;
    --white: #ffffff;
  }
  * { margin: 0; padding: 0; box-sizing: border-box; }
  html, body { width: 882px; height: 1200px; overflow: hidden; }
  body {
    font-family: "M PLUS Rounded 1c", sans-serif;
    color: var(--ink);
    background: var(--white);
  }
  .flyer {
    position: relative;
    width: 882px;
    height: 1200px;
    overflow: hidden;
    background:
      radial-gradient(ellipse at 20% 15%, var(--pink-soft) 0%, transparent 55%),
      radial-gradient(ellipse at 85% 40%, var(--pink-soft) 0%, transparent 50%),
      radial-gradient(ellipse at 30% 80%, var(--pink-wash) 0%, transparent 55%),
      linear-gradient(180deg, var(--pink-wash) 0%, #fdf0f3 60%, var(--pink-wash) 100%);
  }
  .content-panel {
    position: absolute;
    top: 70px; left: 70px;
    width: 742px; height: 860px;
    background: var(--white);
    border: 3px solid var(--pink-line);
    border-radius: 150px 150px 90px 90px;
  }
  .title {
    position: absolute;
    top: 200px; left: 0; right: 0;
    text-align: center;
    font-size: 64px;
    font-weight: 500;
    color: var(--pink);
    letter-spacing: 2px;
    line-height: 1.2;
  }
  .subtitle {
    position: absolute;
    top: 300px; left: 0; right: 0;
    text-align: center;
    font-size: 28px;
    font-weight: 500;
    letter-spacing: 3px;
    line-height: 1.3;
  }
  .visit-car {
    position: absolute;
    top: 375px; left: 245px;
    width: 392px; height: 250px;
    border-radius: 24px;
    background: linear-gradient(160deg, #f6f6f6, #e9e9ea);
  }
  .about-label {
    position: absolute;
    top: 660px; left: 321px;
    width: 240px; height: 32px;
    background: var(--pink);
    color: var(--white);
    font-size: 16px;
    font-weight: 500;
    text-align: center;
    line-height: 32px;
    letter-spacing: 1px;
  }
  .about-text {
    position: absolute;
    top: 706px; left: 311px;
    width: 260px;
    font-size: 13px;
    line-height: 1.75;
    text-align: center;
  }
  .services-heading {
    position: absolute;
    top: 935px; left: 0; right: 0;
    text-align: center;
    font-size: 28px;
    font-weight: 700;
    color: var(--pink-deep);
    letter-spacing: 4px;
    line-height: 1.3;
  }
  .services {
    position: absolute;
    top: 995px; left: 71px;
    display: flex;
    gap: 20px;
    list-style: none;
  }
  .service {
    width: 170px; height: 170px;
    border-radius: 50%;
    background: var(--pink);
    color: var(--white);
    display: flex;
    align-items: center;
    justify-content: center;
    text-align: center;
    font-size: 19px;
    font-weight: 700;
    line-height: 1.45;
  }
</style>
</head>
<body>
<main class="flyer">
  <div class="content-panel" aria-hidden="true"></div>

  <h1 class="title">RPE歯科医院</h1>
  <p class="subtitle">訪問・送迎歯科クリニック</p>

  <div class="visit-car" role="img" aria-label="歯科スタッフ二人が車で訪問に向かうイラスト「いきます」"></div>

  <h2 class="about-label">訪問歯科診療とは</h2>
  <p class="about-text">介護施設やご自宅で過ごされる方や歩行が困難で通院ができない方のもとへ歯科医師や歯科衛生士がお伺いし、診療を行う医療サービスです。</p>

  <h2 class="services-heading">治療内容</h2>
  <ul class="services">
    <li class="service">虫歯・<br>歯周病の<br>治療、予防</li>
    <li class="service">入れ歯の<br>作製、修理、<br>調整</li>
    <li class="service">口腔ケアで<br>感染症予防</li>
    <li class="service">お口の<br>リハビリ</li>
  </ul>
</main>
</body>
</html>
```